Brack and Loam LLC | Land Clearing, Landscaping & Dump Trailer Services

Project Description: Brack and Loam LLC Website Design
The website will be published using squarespace
Objective:
Design a visually compelling and conversion-driven website for Brack and Loam LLC, a land solutions business based in Pickens County, Georgia. The site will highlight the company’s professionalism, locally rooted service, and commitment to quality in land clearing, grading, and dump trailer services.
Pages & Features to Include:
1. Landing Page (Homepage)
- Clear tagline: Shaping Ground with Care and Grit
- Call-to-Action (CTA) buttons: “Get a Free Quote” and “View Services”
- Service highlights with icons or photos (e.g., grading, mulching, hauling)
- Customer testimonials
- Embedded contact form
- Google Maps integration showing service area
2. Services + Pricing Page
- Organized list of services under 3 categories:
- **Land Clearing & Grading**
- Forestry Mulching
- Gravel Driveway Repair
- Minimum Job Fee:
- Dump Trailer Services
- Trailer Rental (Daily):
- Junk Removal (Full Load)
- Material Delivery: $ + mileage
- Specialty Jobs
- Stump removal, light demolition
- Each service section includes short descriptions and photos
- Optional quote form at the bottom with “Request a Quote” CTA
Design Style:
- Clean, professional design using clean tones
- Fonts that balance industrial strength and local charm
- Mobile-optimized with fast loading speeds and easy navigation
- SEO-optimized for terms like *land clearing Pickens County*, *grading services North Georgia*, and *dump trailer rental Jasper GA*, etc...

```html
<!DOCTYPE html>
<html lang="en">
<head>
<meta charset="utf-8">
<title>Brack and Loam LLC | Land Clearing, Grading &amp; Dump Trailer Services</title>
<link rel="stylesheet" href="https://fonts.googleapis.com/css2?family=Krona+One&family=Work+Sans:ital,wght@0,400;0,500;0,600;1,400&display=swap">
<style>
:root{
  --green:#4a9a2e;
  --green-dark:#2f6e1c;
  --green-soft:rgba(62,140,34,.82);
  --ink:#222;
  --text:#666;
  --cream:#f4f6ef;
  --line:#cfcfcf;
  --footer:#2b2b2b;
  --white:#fff;
}
*{box-sizing:border-box;margin:0;padding:0}
html,body{width:1200px;height:3960px;overflow:hidden}
body{font-family:"Work Sans",sans-serif;color:var(--ink);background:var(--white);position:relative}
.abs{position:absolute}
.display{font-family:"Krona One",sans-serif;text-transform:uppercase;letter-spacing:-1px}
.btn{position:absolute;display:flex;align-items:center;padding-left:12px;background:var(--green);color:var(--white);font-family:"Krona One",sans-serif;font-size:14px;text-transform:uppercase;letter-spacing:-.5px;text-decoration:none;white-space:nowrap}

/* header */
.brand{left:122px;top:18px;display:flex;align-items:center;gap:10px;font-weight:600;font-size:16px;color:var(--ink)}
.brand-dot{width:18px;height:18px;background:var(--green);display:block}
.nav{left:298px;top:48px;display:flex;gap:36px;font-size:14px;letter-spacing:.5px;color:#333}
.nav a{color:inherit;text-decoration:none}

/* hero */
.hero-photo{left:0;top:0;width:1200px;height:720px;background:linear-gradient(180deg,#eef2ea 0%,#7a9866 14%,#4d6f36 45%,#6b5a3e 80%,#7b6a4d 100%)}
.hero-wave{left:0;top:620px}
.hero-box{left:95px;top:212px;width:540px;height:318px;background:var(--green-soft)}
.hero-title{left:137px;top:262px;font-size:38px;line-height:48px;color:var(--white);width:480px}

/* services */
.section-title{width:1200px;left:0;text-align:center;font-size:38px;color:var(--ink)}
.section-title span{color:var(--green)}
.card{position:absolute;top:915px;width:295px;height:232px;background:var(--white);border-radius:22px;box-shadow:0 2px 10px rgba(0,0,0,.08)}
.card.featured{border-right:5px solid var(--green)}
.card-icon{position:absolute;left:18px;top:24px;width:78px;height:78px;border-radius:50%;background:var(--green);display:block}
.card-name{position:absolute;left:110px;top:44px;font-size:15px;line-height:19px;color:var(--ink)}
.card p{position:absolute;left:18px;top:110px;width:260px;font-size:13px;line-height:28px;color:var(--text)}
.card a{position:absolute;left:22px;top:198px;font-family:"Krona One",sans-serif;font-size:10px;color:var(--green-dark);text-decoration:underline}

/* about */
.about{left:0;top:1255px;width:1200px;height:618px;background:var(--cream)}
.about-mark{left:165px;top:1360px;width:410px;height:405px;display:flex;align-items:center;gap:14px;justify-content:center}
.about-mark span{font-size:30px;font-weight:600;color:#333}
.about-mark i{width:34px;height:34px;background:var(--green);display:block}
.about-title{left:595px;top:1372px;font-size:38px;line-height:48px;color:var(--ink)}
.about-title span{color:var(--green)}
.about-text{left:595px;top:1482px;width:435px;font-size:13px;line-height:28px;color:var(--text)}

/* testimonials */
.testimonials{left:0;top:1873px;width:1200px;height:617px;background:radial-gradient(ellipse at 50% 40%,#5fa83e 0%,#3f8a24 60%,#2f7219 100%)}
.quote-card{position:absolute;top:2073px;width:296px;height:320px;background:var(--white);padding:28px 22px}
.quote-mark{font-family:Georgia,serif;font-size:80px;line-height:60px;color:transparent;-webkit-text-stroke:1.5px var(--green);height:50px}
.quote-card p{margin-top:6px;font-style:italic;font-size:15px;line-height:28px;color:#777}
.quote-card cite{display:block;margin-top:4px;font-style:normal;font-weight:600;font-size:15px;color:var(--green);padding-left:6px}

/* contact */
.field{position:absolute;border:1.5px solid var(--line);font-size:14px;color:#999;padding:14px}

/* map + footer */
.map{left:0;top:3030px;width:1200px;height:480px;background:linear-gradient(135deg,#e6e6e6,#d6d6d6 50%,#e2e2e2)}
.map-card{left:490px;top:3180px;width:262px;height:128px;background:var(--white);border-radius:6px;box-shadow:0 3px 12px rgba(0,0,0,.15);padding:26px 24px;font-size:14px;line-height:28px;color:#444}
.map-card a{color:var(--green);text-decoration:none}
.footer{left:0;top:3450px;width:1200px;height:510px;background:var(--footer)}
.foot-brand{left:130px;top:3660px;display:flex;align-items:center;gap:10px;font-weight:600;font-size:18px;color:var(--white)}
.foot-brand i{width:18px;height:18px;background:var(--green);display:block}
.foot-col{top:3600px;color:var(--white)}
.foot-col h3{font-family:"Krona One",sans-serif;font-size:19px;letter-spacing:-.8px;text-transform:uppercase;margin-bottom:14px}
.foot-col li{list-style:none;font-size:15px;line-height:28px}
.foot-contact li{display:flex;gap:12px;align-items:flex-start;margin-bottom:4px}
.foot-contact svg{flex:none;margin-top:7px}
.divider{left:108px;top:3817px;width:984px;height:1px;background:#555}
.copy{left:0;width:1200px;top:3848px;text-align:center;font-size:14px;color:var(--white)}
.social{left:520px;top:3882px;display:flex;gap:10px}
.social i{width:32px;height:32px;border-radius:50%;border:2px solid var(--white);display:block}
.social i:first-child{background:var(--green);border-color:var(--green)}
</style>
</head>
<body>

<div class="abs hero-photo" role="img" aria-label="Photo of a red compact track loader with a dirt bucket in a cleared pine forest"></div>
<svg class="abs hero-wave" width="1200" height="130" viewBox="0 0 1200 130" aria-hidden="true">
  <path d="M0 30 L20 80 L160 70 L240 40 L300 20 L420 50 L560 60 L640 95 L760 90 L880 70 L1000 55 L1100 70 L1200 40 V130 H0Z" fill="#fff"/>
  <path d="M0 30 L20 80 L160 70 L240 40 L300 20 L420 50 L560 60 L640 95 L760 90 L880 70 L1000 55 L1100 70 L1200 40" fill="none" stroke="var(--green)" stroke-width="9"/>
</svg>

<header>
  <div class="abs brand"><i class="brand-dot"></i>Brack and Loam LLC</div>
  <nav class="abs nav"><a href="#">HOME</a><a href="#">ABOUT US</a><a href="#">SERVICES</a><a href="#">PRICING</a><a href="#">CONTACT US</a></nav>
  <a class="btn" href="#" style="left:842px;top:35px;width:235px;height:45px">Get a Free Quote</a>
</header>

<div class="abs hero-box"></div>
<h1 class="abs hero-title display">Shaping Ground with Care and Grit.</h1>
<a class="btn" href="#" style="left:137px;top:430px;width:233px;height:42px">Get a Free Quote</a>
<a class="btn" href="#" style="left:376px;top:430px;width:216px;height:42px">View Services</a>

<h2 class="abs section-title display" style="top:822px"><span>Our</span> Services</h2>
<div class="card" style="left:143px"><i class="card-icon"></i><h3 class="card-name display">Small-Scale<br>Grading</h3><p>Lorem ipsum dolor sit amet, consectetur adipiscing elit, sed do eiusmod tempor incididunt ut.</p><a href="#">Learn More</a></div>
<div class="card featured" style="left:454px"><i class="card-icon"></i><h3 class="card-name display">Land<br>Clearing</h3><p>Lorem ipsum dolor sit amet, consectetur adipiscing elit, sed do eiusmod tempor incididunt ut.</p><a href="#">Learn More</a></div>
<div class="card" style="left:763px"><i class="card-icon"></i><h3 class="card-name display">Dump Trailer<br>Services.</h3><p>Lorem ipsum dolor sit amet, consectetur adipiscing elit, sed do eiusmod tempor incididunt ut.</p><a href="#">Learn More</a></div>

<section class="abs about"></section>
<div class="abs about-mark"><i></i><span>Brack and Loam LLC</span></div>
<h2 class="abs about-title display"><span>About</span> Brack<br>and Loam LLC.</h2>
<div class="abs about-text">
  <p>Lorem ipsum dolor sit amet, consectetur adipiscing elit, sed do eiusmod tempor incididunt ut.iste natus error sit voluptatem accusantium doloremque laudantium, totam rem aperiam, eaque ipsa quae ab illo inventore veritatis et quasi architecto beatae vitae dicta sunt explicabo.</p>
  <p>Nemo enim ipsam voluptatem quia voluptas sit aspernatur aut odit aut fugit, sed quia consequuntur magni dolores eos qui ratione voluptatem sequi nesciunt.</p>
</div>
<a class="btn" href="#" style="left:595px;top:1720px;width:235px;height:42px">Get a Free Quote</a>

<section class="abs testimonials" role="img" aria-label="Green-tinted photo of a forest clearing"></section>
<h2 class="abs section-title display" style="top:1958px;color:#fff;line-height:48px">Our Customers<br>Testimonials</h2>
<blockquote class="quote-card" style="left:144px"><div class="quote-mark">“</div><p>“ Lorem ipsum dolor sit amet, consectetur adipiscing elit, sed do eiusmod tempor incididunt ut labore et dolore magna aliqua. Quis ipsum suspendisse ultrices gravida. Risus commodo viverra maecenas accumsan.”</p><cite>- Dana Whitfield</cite></blockquote>
<blockquote class="quote-card" style="left:452px"><div class="quote-mark">“</div><p>“ Lorem ipsum dolor sit amet, consectetur adipiscing elit, sed do eiusmod tempor incididunt ut labore et dolore magna aliqua. Quis ipsum suspendisse ultrices gravida. Risus commodo viverra maecenas accumsan.”</p><cite>- Dana Whitfield</cite></blockquote>
<blockquote class="quote-card" style="left:760px"><div class="quote-mark">“</div><p>“ Lorem ipsum dolor sit amet, consectetur adipiscing elit, sed do eiusmod tempor incididunt ut labore et dolore magna aliqua. Quis ipsum suspendisse ultrices gravida. Risus commodo viverra maecenas accumsan.”</p><cite>- Dana Whitfield</cite></blockquote>

<h2 class="abs section-title display" style="top:2616px"><span>Contact</span> Us</h2>
<div class="field" style="left:187px;top:2700px;width:270px;height:46px">Full Name</div>
<div class="field" style="left:465px;top:2700px;width:270px;height:46px">Email Address</div>
<div class="field" style="left:743px;top:2700px;width:270px;height:46px">Phone Number</div>
<div class="field" style="left:187px;top:2756px;width:826px;height:94px">Message</div>
<a class="btn" href="#" style="left:499px;top:2885px;width:201px;height:44px;padding-left:10px">Submit Now</a>

<div class="abs map" role="img" aria-label="Map of the service area with location pins"></div>
<div class="abs map-card">
  <svg width="12" height="16" viewBox="0 0 12 16" style="vertical-align:-2px"><path d="M6 0a6 6 0 0 1 6 6c0 4.5-6 10-6 10S0 10.5 0 6a6 6 0 0 1 6-6z" fill="var(--green)"/><circle cx="6" cy="6" r="2.3" fill="#fff"/></svg>
  123, Street name, city name<br>&nbsp;&nbsp;&nbsp;united state - 123 456.<br>&nbsp;&nbsp;&nbsp;<a href="#">View more</a>
</div>
<svg class="abs" style="left:566px;top:3092px" width="60" height="80" viewBox="0 0 60 80" aria-hidden="true"><path d="M30 0a30 30 0 0 1 30 30c0 22-30 50-30 50S0 52 0 30A30 30 0 0 1 30 0z" fill="var(--green)"/><circle cx="30" cy="29" r="19" fill="#fff"/></svg>

<svg class="abs" style="left:0;top:3420px" width="1200" height="80" viewBox="0 0 1200 80" aria-hidden="true">
  <path d="M0 40 L120 20 L260 35 L420 22 L560 50 L700 45 L820 60 L960 30 L1080 10 L1200 5 V80 H0Z" fill="var(--footer)"/>
  <path d="M0 40 L120 20 L260 35 L420 22 L560 50 L700 45 L820 60 L960 30 L1080 10 L1200 5" fill="none" stroke="var(--green)" stroke-width="9"/>
</svg>
<footer>
  <div class="abs footer" role="img" aria-label="Dark photo of heavy equipment"></div>
  <div class="abs foot-brand"><i></i>Brack and Loam LLC</div>
  <div class="abs foot-col" style="left:355px"><h3>Quick Links</h3><ul><li>Home</li><li>About us</li><li>Services</li><li>Pricing</li><li>Contact us</li></ul></div>
  <div class="abs foot-col" style="left:583px"><h3>Other Links</h3><ul><li>Privacy Policy</li><li>Terms and Condition</li><li>Testimonials</li><li>FAQ</li></ul></div>
  <div class="abs foot-col foot-contact" style="left:820px"><h3>Contact Us</h3><ul>
    <li><svg width="10" height="14" viewBox="0 0 12 16"><path d="M6 0a6 6 0 0 1 6 6c0 4.5-6 10-6 10S0 10.5 0 6a6 6 0 0 1 6-6z" fill="var(--green)"/></svg><span>Fernbrook, OR, United States,<br>Oregon.</span></li>
    <li><svg width="13" height="10" viewBox="0 0 13 10"><rect width="13" height="10" rx="1" fill="var(--green)"/><path d="M0 1l6.5 5L13 1" stroke="#2b2b2b" fill="none"/></svg><span>hello@brackandloam.com</span></li>
    <li><svg width="12" height="12" viewBox="0 0 12 12"><path d="M2 0l2.5 2.5-1.3 1.8a8 8 0 0 0 4.5 4.5l1.8-1.3L12 10l-2 2C4.5 12 0 7.5 0 2z" fill="var(--green)"/></svg><span>+1 555-010-4821</span></li>
  </ul></div>
  <div class="abs divider"></div>
  <p class="abs copy">2025 Copyrights © Brack and Loam LLC &nbsp;|&nbsp; All Rights Reserved</p>
  <div class="abs social"><i></i><i></i><i></i><i></i></div>
</footer>

</body>
</html>
```